Establishing a website for a non profit organisation

The foundation is called:

German: Edle Betagte Vereinigung des Hauses Lindmark e.V.

Englisch (Translation): Noble venerable Union of House Lindmark e.V.

The foundation is a legal nonprofit organization with the purpose to help people in need. The foundation - a charitable organization - donates funds and supports solely and directly people living in Frankfurt and in Germany.

In some cases the foundation works together with other charitable organizations that support projects to help people in need.

The foundation also functions as trustee with powers of administration of property in trust with a legal obligation to administer it solely for the purposes specified. The purpose is not to generate/obtain wealth for shareholders but to respectfully execute the benevolent intentions of the founders/testators in the interest of the legatee.

The foundation was established in 1408.

The website should give a good and easy overview about the foundation work.
It should be easy to figure out how to participate and help the organisation.
Either you can participate with a one time donation, with a regular donation or with a testament.

For those with donation it is possible to hand over an contribution receipt for tax purposes.

The main color should be red: RGB R:229 - G:47 - B:34

```html
<!DOCTYPE html>
<html lang="en">
<head>
<meta charset="utf-8">
<title>EBVHL e.V – Noble venerable Union of House Lindmark</title>
<link href="https://fonts.googleapis.com/css2?family=Nunito+Sans:wght@300;400;600&display=swap" rel="stylesheet">
<style>
:root{
  --red:#e52f22;
  --dark:#3a3a3a;
  --text:#222;
  --muted:#666;
  --line:#dcdcdc;
  --footer:#ececec;
}
*{margin:0;padding:0;box-sizing:border-box}
html,body{width:821px;height:1200px;overflow:hidden;background:#fff}
body{position:relative;font-family:"Nunito Sans",Arial,sans-serif;color:var(--text)}
.abs{position:absolute}
.logo{left:50px;top:0;width:124px;height:57px;background:var(--red);color:#fff;text-align:center;font-weight:400;font-size:24px;line-height:23px;padding-top:6px}
.logo small{display:block;font-size:19px}
.head-rule{left:50px;top:57px;width:720px;height:2px;background:var(--red)}
.search{left:605px;top:17px;width:165px;height:26px;border:1px solid var(--line);background:#f7f7f7;font-size:8px;font-style:italic;color:#999;padding:8px 9px}
.search-btn{right:2px;top:3px;width:18px;height:18px;background:#222;border-radius:2px}
.nav{left:50px;top:66px;width:720px;height:32px;background:var(--dark);display:flex;justify-content:space-between}
.nav a{flex:none;white-space:nowrap;color:#fff;text-decoration:none;font-size:9.3px;line-height:32px;padding:0 12.5px;letter-spacing:.2px}
.nav a.active{background:var(--red);padding:0 15px}
.hero{left:50px;top:102px;width:720px;height:278px;background:radial-gradient(ellipse at 52% 55%,#9a9a9a 0%,#5a5a5a 40%,#2a2a2a 100%)}
.dots{left:335px;top:253px;display:flex;gap:4px}
.dots i{width:9px;height:9px;border-radius:50%;background:#111;display:block}
.dots i:first-child{background:var(--red)}
.tax{left:79px;top:405px;font-size:21px;font-weight:300;color:#555;letter-spacing:.2px;white-space:nowrap}
.btn-donate{left:600px;top:399px;width:142px;height:37px;background:var(--red);color:#fff;font-size:15px;line-height:37px;text-align:center;letter-spacing:.5px}
.rule{left:50px;width:720px;height:2px;background:var(--line)}
h2{font-weight:300;font-size:16px;color:var(--red);letter-spacing:.2px;white-space:nowrap}
.mission{left:50px;top:477px;width:470px;font-size:16px;line-height:22px;white-space:normal}
.mission span{color:var(--text)}
.lead{left:50px;top:525px;width:470px;font-size:8.8px;line-height:14.5px;color:#111}
.body{font-size:8.8px;line-height:14.5px;color:var(--muted);font-weight:300}
.btn-dark{background:var(--dark);color:#fff;font-size:8px;height:22px;line-height:22px;padding:0 8px;white-space:nowrap}
.btn-red{background:var(--red);color:#fff;font-size:8px;height:22px;line-height:22px;padding:0 9px;white-space:nowrap}
.link-red{color:var(--red);font-size:8px}
.photo{display:block}
.vline{width:1px;background:var(--line)}
.proj-h{color:var(--red);font-size:8.5px}
.footer{left:0;top:1108px;width:821px;height:92px;background:var(--footer)}
.social{display:flex;gap:5px}
.social i{width:20px;height:20px;border-radius:50%;background:#9a9a9a;display:block}
</style>
</head>
<body>
<header>
  <div class="abs logo">EBVHL<small>e.V</small></div>
  <div class="abs head-rule"></div>
  <div class="abs search">Search...<span class="abs search-btn"><svg width="18" height="18" viewBox="0 0 18 18"><circle cx="7.5" cy="7.5" r="3.5" fill="none" stroke="#fff" stroke-width="1.6"/><line x1="10" y1="10" x2="14" y2="14" stroke="#fff" stroke-width="2"/></svg></span></div>
  <nav class="abs nav">
    <a class="active">HOME</a><a>WHO WE ARE</a><a>WHAT WE DO</a><a>MAKE DONATION</a><a>OUR PROJECTS</a><a>NEWS &amp; PRESS</a><a>BLOG</a><a>SUPPORTS</a><a>CONTACT US</a>
  </nav>
</header>

<section class="abs hero" role="img" aria-label="Black and white photo of cupped hands holding copper coins"></section>
<div class="abs dots"><i></i><i></i><i></i><i></i></div>

<div class="abs tax">DONATION YOU MAKE ARE EXEMPTED FROM TAX</div>
<div class="abs btn-donate">DONATE NOW</div>
<div class="abs rule" style="top:451px"></div>

<h2 class="abs mission"><span>OUR MISSION</span> IS TO HELP THOSE WHO NEED IT! CHANGE THE LIFE OF THOSE, WHO HAVE NO HOPE!</h2>
<p class="abs lead">Nasceus mus. Nulla dui. Fusce feugiat malesuada odio. Scing elit. Mauris fermentum dictum gna. Sed laoreet aliquameo. Ut us dolor, dapibus eget elementum vel, cursus.</p>
<p class="abs body" style="left:50px;top:562px;width:470px">Nasceus mus. Nulla dui. Fusce feugiat malesuada odio. Scing elit. Mauris fermentum dictum gna. Sed laoreet aliquameo. Ut us dolor, dapibus eget elementum vel, cursus eleifendeneanctor wisi et urna. Aliquam erat volutpat.Duis ac turpis. Integer rutrum ante eu uisque nulla. Fuscegiat malesuada odio.  fermentum dictum gna.</p>
<div class="abs btn-dark" style="left:50px;top:621px">READ MORE ››</div>
<div class="abs photo" style="left:543px;top:481px;width:227px;height:162px;background:linear-gradient(90deg,#b08a5a 0 19%,#c8242a 19% 62%,#b08a5a 62%)" role="img" aria-label="Magnifying glass over a red charity label"></div>
<div class="abs rule" style="top:667px;height:1px"></div>

<h2 class="abs" style="left:51px;top:682px">WHAT WE DO</h2>
<div class="abs photo" style="left:50px;top:711px;width:213px;height:108px;background:linear-gradient(120deg,#6f86a8,#b89a78 55%,#8a6a4a)" role="img" aria-label="Volunteers at a food drive holding a cardboard donation sign"></div>
<p class="abs body" style="left:51px;top:831px;width:212px">Nasceus mus. Nulla dui. Fusce feugiat malesuada odio. Scing elit. Mauris fermentum dictum gna. Sed laoreet aliquameo. Ut us dolor, dapibus eget elementum vel. cursus eleifendeneanctor..</p>
<div class="abs btn-dark" style="left:51px;top:904px">READ MORE ››</div>
<div class="abs vline" style="left:276px;top:684px;height:242px"></div>

<h2 class="abs" style="left:297px;top:682px">OUR PROJECTS</h2>
<div class="abs photo" style="left:297px;top:711px;width:149px;height:95px;background:linear-gradient(135deg,#d8d8d8,#555)" role="img" aria-label="Black and white photo of many joined hands"></div>
<div class="abs photo" style="left:459px;top:711px;width:149px;height:95px;background:linear-gradient(135deg,#a89a8a,#e4d8c8)" role="img" aria-label="Volunteers and a child holding a thank you sign"></div>
<div class="abs photo" style="left:622px;top:711px;width:148px;height:95px;background:linear-gradient(180deg,#8fb57a,#6a7a8a)" role="img" aria-label="Crowd gathered at an outdoor charity event"></div>

<div class="abs" style="left:297px;top:820px;width:149px"><div class="proj-h">PROJECT HEADING</div><p class="body">Nasceus mus. Nulla dui. Fusce feugiat malesuada odio. Scing elit. Mauris fermentum dictum gna. Sed laoreet aliquameo.</p></div>
<div class="abs" style="left:459px;top:820px;width:149px"><div class="proj-h">PROJECT HEADING</div><p class="body">Nasceus mus. Nulla dui. Fusce feugiat malesuada odio. Scing elit. Mauris fermentum dictum gna. Sed laoreet aliquameo.</p></div>
<div class="abs" style="left:622px;top:820px;width:149px"><div class="proj-h">PROJECT HEADING</div><p class="body">Nasceus mus. Nulla dui. Fusce feugiat malesuada odio. Scing elit. Mauris fermentum dictum gna. Sed laoreet aliquameo.</p></div>
<div class="abs btn-dark" style="left:297px;top:904px">READ MORE ››</div>
<div class="abs btn-dark" style="left:459px;top:904px">READ MORE ››</div>
<div class="abs btn-dark" style="left:622px;top:904px">READ MORE ››</div>
<div class="abs rule" style="top:952px;height:1px"></div>

<h2 class="abs" style="left:51px;top:971px">LATEST NEWS</h2>
<div class="abs" style="left:51px;top:1001px;width:215px">
  <div style="font-size:8.5px;color:#111">AUG 04, 2014</div>
  <p class="body">Nasceus mus. Nulla dui. Fusce feugiat malesuada odio. Scing elit. Mauris fermentum dictum gna. Sed laoreet aliquameo...</p>
  <div class="link-red" style="margin-top:10px">READ MORE ››</div>
</div>
<div class="abs vline" style="left:289px;top:974px;height:114px"></div>

<h2 class="abs" style="left:307px;top:971px">BLOG POSTS</h2>
<div class="abs" style="left:307px;top:1001px;width:210px">
  <div style="font-size:8.5px;line-height:13px;color:#111;font-weight:600">Fusce feugiat malesuada odio.Scing elit. Mauris fermentu...</div>
  <div style="font-size:8px;color:var(--red);font-style:italic;margin:1px 0 4px">Posted on 2 days ago</div>
  <p class="body">Nasceus mus. Nulla dui. Fusce feugiat malesuada odio. Scing elit. Mauris fermentum dictum gna.</p>
  <div class="link-red" style="margin-top:10px">READ MORE ››</div>
</div>
<div class="abs vline" style="left:536px;top:974px;height:114px"></div>

<h2 class="abs" style="left:553px;top:971px">NEWSLETTER SIGN UP</h2>
<p class="abs body" style="left:554px;top:999px;width:216px">Nasceus mus. Nulla dui. Fusce feugiat malesuada odio. Scing elit. Mauris fermentum dictum gna.</p>
<div class="abs" style="left:553px;top:1039px;width:217px;height:27px;border:1px solid var(--line);border-radius:2px;font-size:7.5px;color:#999;padding:9px 10px">Enter Email Address</div>
<div class="abs btn-red" style="left:697px;top:1076px">SUBSCRIBE ››</div>

<footer class="abs footer">
  <div class="abs" style="left:50px;top:32px;font-size:7.5px;line-height:14.5px;color:#444;white-space:nowrap">Copyright © 2014. <span style="color:var(--red)">EBVHL e.V.</span> All Right Reserved<br>Privacy Policy</div>
  <div class="abs" style="left:700px;top:16px;font-size:9.5px;color:#333;white-space:nowrap">Connect Us:</div>
  <div class="abs social" style="left:699px;top:37px"><i aria-label="Social link"></i><i aria-label="Social link"></i><i aria-label="Feed link"></i></div>
</footer>
</body>
</html>
```